Company or website name
- Marla Quade Design & Decor
- Links to the website
- Passionate about wedding floral design and decor. Events I create are timeless, classic and elegant, customized 100% to the brides’ desires. Inspiring them with a vision of what is possible & asking them to step inside it and see it for themselves
- Other Facts

```html
<!DOCTYPE html>
<html lang="en">
<head>
<meta charset="utf-8">
<title>Marla Quade Design &amp; Decor — Stationery Set</title>
<link rel="stylesheet" href="https://fonts.googleapis.com/css2?family=Cinzel:wght@400&family=Tinos:wght@400&display=swap">
<style>
  :root {
    --pink: #f2c6ee;
    --pink-soft: #f6d6f3;
    --pink-deep: #e9b3e4;
    --white: #ffffff;
    --paper: #ffffff;
    --ink: #222222;
    --ground: #eeeeee;
    --shadow: rgba(0,0,0,0.18);
  }
  * { box-sizing: border-box; margin: 0; padding: 0; }
  html, body { width: 1132px; height: 1200px; overflow: hidden; }
  body { background: var(--ground); font-family: "Tinos", "Times New Roman", serif; position: relative; }
  address { font-style: normal; }

  .sheet { position: absolute; box-shadow: 0 6px 18px var(--shadow); }

  /* Letterhead */
  .letterhead { left: 60px; top: 150px; width: 500px; height: 707px; background: var(--paper); }
  .letterhead .sender { position: absolute; left: 300px; top: 40px; font-size: 12px; line-height: 1.35; color: var(--ink); }
  .letterhead .sender .email { margin-top: 16px; }
  .letterhead .footer-band { position: absolute; left: 0; right: 0; top: 585px; height: 62px; background: var(--pink); display: flex; align-items: center; padding-left: 40px; gap: 14px; }
  .letterhead .footer-band::before, .letterhead .footer-band::after { content: ""; position: absolute; left: 0; right: 0; height: 2px; background: var(--white); }
  .letterhead .footer-band::before { top: 6px; }
  .letterhead .footer-band::after { bottom: 6px; }
  .letterhead .website { position: absolute; right: 24px; top: 660px; font-size: 15px; color: var(--ink); }

  .brand-name { font-family: "Tinos", "Times New Roman", serif; color: var(--white); text-align: center; line-height: 1.15; }
  .ornament { display: block; }

  /* Logo tag */
  .logo-tag { left: 620px; top: 50px; width: 300px; height: 130px; background: var(--pink); border-radius: 14px; border: 3px solid var(--white); outline: 2px solid var(--pink-deep); display: flex; align-items: center; justify-content: center; }
  .logo-tag .brand-name { font-size: 26px; }
  .logo-tag .ornament { position: absolute; right: -106px; top: -16px; }

  /* Business card front */
  .card-front { left: 600px; top: 250px; width: 470px; height: 290px; background: var(--pink); overflow: hidden; }
  .card-front .pattern { position: absolute; inset: 0; }
  .card-front .stripe { position: absolute; left: 0; right: 0; top: 98px; height: 96px; border-top: 3px solid var(--white); border-bottom: 3px solid var(--white); background: var(--pink); }
  .card-front .stripe::before { content: ""; position: absolute; left: 0; right: 0; top: 6px; bottom: 6px; border-top: 1px solid var(--white); border-bottom: 1px solid var(--white); }
  .card-front .label { position: absolute; left: 125px; top: 80px; width: 220px; height: 130px; background: var(--pink); border: 3px solid var(--white); border-radius: 14px; display: flex; align-items: center; justify-content: center; }
  .card-front .label .brand-name { font-size: 23px; }
  .card-front .ornament.left { position: absolute; left: 40px; top: 150px; }
  .card-front .ornament.right { position: absolute; right: 30px; top: 100px; }

  /* Card back */
  .card-back { left: 590px; top: 585px; width: 480px; height: 330px; background: var(--pink); }
  .card-back .sender { position: absolute; left: 18px; top: 24px; font-size: 9px; line-height: 1.4; color: var(--white); }
  .card-back .headline { position: absolute; left: 108px; top: 58px; font-family: "Cinzel", "Times New Roman", serif; color: var(--white); }
  .card-back .headline .name { font-size: 38px; letter-spacing: 1px; line-height: 1; }
  .card-back .headline .title { font-size: 18px; letter-spacing: 6px; margin-top: 4px; }
  .card-back .email { position: absolute; right: 40px; top: 136px; font-size: 11px; color: var(--white); }
  .card-back .rule { position: absolute; left: 0; right: 0; top: 230px; height: 1px; background: var(--white); }
  .card-back .mini-label { position: absolute; left: 60px; top: 260px; display: flex; align-items: center; gap: 10px; }
  .card-back .mini-label .brand-name { font-size: 13px; }
  .card-back .website { position: absolute; right: 20px; top: 300px; font-size: 10px; color: var(--white); }
</style>
</head>
<body>

<section class="sheet letterhead" aria-label="Letterhead">
  <address class="sender">
    Marla Quade<br>
    14 Linden Row<br>
    Ashford Vale<br>
    AV2 7KL<br>
    Tel. 0412-555-019<br>
    Fax. 041-255-5020
    <div class="email">hello@marlaquadedecor.com</div>
  </address>
  <div class="footer-band">
    <div class="brand-name" style="font-size:15px;">Marla Quade<br>Design &amp; Decor</div>
    <svg class="ornament" width="60" height="40" role="img" aria-label="White floral swirl ornament">
      <rect width="60" height="40" rx="8" fill="#f9e6f7"/>
    </svg>
  </div>
  <div class="website">www.marlaquadedecor.com</div>
</section>

<section class="sheet logo-tag" aria-label="Brand tag">
  <div class="brand-name">Marla Quade<br>Design &amp; Decor</div>
  <svg class="ornament" width="90" height="90" role="img" aria-label="Grey floral swirl ornament">
    <rect width="90" height="90" rx="20" fill="#dcdcdc" opacity="0.7"/>
  </svg>
</section>

<section class="sheet card-front" aria-label="Business card front">
  <svg class="pattern" width="470" height="290" role="img" aria-label="Soft white damask pattern on pink">
    <rect width="470" height="290" fill="#f4cff0"/>
  </svg>
  <div class="stripe"></div>
  <svg class="ornament left" width="70" height="50" role="img" aria-label="White floral swirl ornament">
    <rect width="70" height="50" rx="10" fill="#f9e6f7"/>
  </svg>
  <svg class="ornament right" width="70" height="50" role="img" aria-label="White floral swirl ornament">
    <rect width="70" height="50" rx="10" fill="#f9e6f7"/>
  </svg>
  <div class="label">
    <div class="brand-name">Marla Quade<br>Design &amp; Decor</div>
  </div>
</section>

<section class="sheet card-back" aria-label="Business card back">
  <address class="sender">
    Marla Quade<br>
    14 Linden Row<br>
    Ashford Vale<br>
    AV2 7KL<br>
    Tel. 0412-555-019<br>
    Fax. 041-255-5020
  </address>
  <div class="headline">
    <div class="name">Marla Quade</div>
    <div class="title">Creative Advisor</div>
  </div>
  <div class="email">hello@marlaquadedecor.com</div>
  <div class="rule"></div>
  <div class="mini-label">
    <div class="brand-name">Marla Quade<br>Design &amp; Decor</div>
    <svg class="ornament" width="40" height="28" role="img" aria-label="White floral swirl ornament">
      <rect width="40" height="28" rx="6" fill="#f9e6f7"/>
    </svg>
  </div>
  <div class="website">www.marlaquadedecor.com</div>
</section>

</body>
</html>
```